Business Card Design

Quorvel Software Limited develops and sells venue and event management software called Quorvel Stagehand, which is available in the cloud or on-premise. The company was established in 1986. Most of our customers are performing arts venues, museums and festivals. Our existing design is a bit dull. We need to convey that we are both innovative and reliable.
Not all our people show their mobile phone numbers on their cards, so the design needs to work land line and mobile or land line only.

Industry/Entity Type

Software

Contact Information for Business Card

Helen Trasko
Director
Quorvel Software Limited
42B Milbrook Lane, Epsom, Surrey, KT19 4DN
Telephone: +44 (0)1372 640913
Mobile: +44 (0)7945 216804
Email: htrasko@quorvel.net
Web: www.quorvel.net

```html
<!DOCTYPE html>
<html lang="en">
<head>
<meta charset="utf-8">
<title>Quorvel Software Limited – Business Card</title>
<link rel="stylesheet" href="https://fonts.googleapis.com/css2?family=Open+Sans:wght@400;600;700;800&display=swap">
<style>
  :root {
    --navy-deep: #0e2a4a;
    --navy: #15385f;
    --steel: #3d6d96;
    --steel-light: #4f86b5;
    --grey-mark: #b8bcc4;
    --ink: #2a2f36;
    --rule: #2f5c86;
    --paper: #ffffff;
    --backdrop: #e7e8ea;
  }
  * { box-sizing: border-box; margin: 0; padding: 0; }
  html, body { width: 1200px; height: 913px; overflow: hidden; }
  body {
    background: var(--backdrop);
    font-family: "Open Sans", Arial, sans-serif;
    position: relative;
  }
  .card {
    position: absolute;
    width: 580px;
    height: 332px;
    box-shadow: 0 6px 18px rgba(0,0,0,0.18);
  }

  /* Front */
  .card-front {
    left: 60px;
    top: 90px;
    background: linear-gradient(160deg, var(--steel) 0%, var(--navy) 45%, var(--navy-deep) 100%);
    display: flex;
    align-items: center;
    justify-content: center;
    gap: 18px;
  }
  .card-front .brand-square {
    width: 44px; height: 44px;
    background: var(--paper);
  }
  .card-front .brand-name {
    color: var(--paper);
    font-weight: 800;
    font-size: 50px;
    letter-spacing: 2px;
  }

  /* Back */
  .card-back {
    left: 560px;
    top: 480px;
    background: var(--paper);
  }
  .card-back .brand-block {
    position: absolute;
    left: 50px;
    top: 120px;
    width: 150px;
    height: 150px;
    background: var(--navy);
  }
  .card-back .details {
    position: absolute;
    left: 250px;
    top: 34px;
    width: 300px;
  }
  .brand-title {
    color: var(--navy);
    font-weight: 800;
    font-size: 30px;
    letter-spacing: 1.5px;
    line-height: 1;
  }
  .brand-sub {
    color: var(--steel-light);
    font-weight: 600;
    font-size: 15px;
    margin-top: 4px;
    margin-left: 24px;
  }
  .rule {
    height: 1px;
    background: var(--rule);
    margin: 12px 0;
  }
  .person {
    font-size: 14px;
    color: var(--steel);
    font-weight: 700;
  }
  .person .role {
    font-weight: 400;
    font-size: 11px;
    color: var(--steel-light);
    margin-left: 6px;
  }
  .contacts { list-style: none; margin-top: 8px; }
  .contacts li {
    display: flex;
    align-items: center;
    gap: 10px;
    font-size: 12.5px;
    color: var(--ink);
    line-height: 21px;
  }
  .contacts svg { width: 13px; height: 13px; fill: var(--ink); flex: none; }
  .address {
    font-size: 12.5px;
    color: var(--ink);
  }
</style>
</head>
<body>
  <section class="card card-front" aria-label="Card front">
    <span class="brand-square"></span>
    <span class="brand-name">QUORVEL</span>
  </section>

  <section class="card card-back" aria-label="Card back">
    <div class="brand-block"></div>
    <div class="details">
      <div class="brand-title">QUORVEL</div>
      <div class="brand-sub">Software Limited</div>
      <div class="rule"></div>
      <div class="person">Helen Trasko<span class="role">Director</span></div>
      <ul class="contacts">
        <li>
          <svg viewBox="0 0 16 16"><path d="M3 1l3 3-2 2c1 2 3 4 6 6l2-2 3 3-2 2C7 14 2 9 1 3z"/></svg>
          +44 (0)1372 640913
        </li>
        <li>
          <svg viewBox="0 0 16 16"><path d="M4 0h8v16H4zM5.5 2v10h5V2zM7 13.5h2v1H7z" fill-rule="evenodd"/></svg>
          +44 (0)7945 216804
        </li>
        <li>
          <svg viewBox="0 0 16 16"><path d="M0 3h16v10H0zM1.5 4.5l6.5 5 6.5-5v7h-13z" fill-rule="evenodd"/></svg>
          htrasko@quorvel.net
        </li>
        <li>
          <svg viewBox="0 0 16 16"><circle cx="8" cy="8" r="7" fill="none" stroke="#2a2f36" stroke-width="1.5"/><ellipse cx="8" cy="8" rx="3" ry="7" fill="none" stroke="#2a2f36" stroke-width="1.2"/><path d="M1 8h14" stroke="#2a2f36" stroke-width="1.2"/></svg>
          www.quorvel.net
        </li>
      </ul>
      <div class="rule"></div>
      <div class="address">42B Milbrook Lane, Epsom, Surrey, KT19 4DN</div>
    </div>
  </section>
</body>
</html>
```